Marlow Hire Business Card for recruitment company

We are looking for a Business Card Design that incorporates our personal details and our busines name and logo. We are a specialized search consultancy that recruit Property and Construction professionals.
We would like a business card that stands out and is appealing to the Construction and Property industry as well.

Target Market(s)

people in the construction and property industry

Contact Information for Business Card

Business Name and logo

Font styles to use
Serif

Colors
0094D4
00A9DD
6FCCEA
C7EBF8
E9F6FB

Requirements
Must have
• Business name and logo as well as contact details
Should not have
• No photos of us please

```html
<!DOCTYPE html>
<html lang="en">
<head>
<meta charset="utf-8">
<title>Marlow Hire – Business Card</title>
<link rel="stylesheet" href="https://fonts.googleapis.com/css2?family=Open+Sans:wght@300;400;700&display=swap">
<style>
  :root {
    --stage: #1d1f21;
    --paper: #f4f5f5;
    --paper-edge: #e4e6e7;
    --teal: #0b6478;
    --teal-light: #0d7388;
    --teal-deep: #06475a;
    --ink: #3a3f42;
    --white: #ffffff;
    --url-white: #d8e6ea;
    --mark-tint-front: rgba(11, 100, 120, 0.22);
    --mark-tint-back: rgba(255, 255, 255, 0.18);
  }
  * { box-sizing: border-box; margin: 0; padding: 0; }
  html, body {
    width: 1200px; height: 900px; overflow: hidden;
    background: var(--stage);
    font-family: "Open Sans", Arial, sans-serif;
  }
  .canvas {
    position: relative; width: 1200px; height: 900px;
    display: flex; flex-direction: column; align-items: center; justify-content: center; gap: 36px;
  }
  .card {
    position: relative; width: 700px; height: 400px; border-radius: 24px; overflow: hidden;
  }
  .brand-mark-area {
    position: absolute; width: 420px; height: 420px; border-radius: 50%;
  }
  /* Front */
  .card--front {
    background: linear-gradient(135deg, var(--white) 0%, var(--paper) 60%, var(--paper-edge) 100%);
    padding: 58px 64px;
    color: var(--ink);
  }
  .card--front .brand-mark-area {
    right: -150px; bottom: -170px;
    background: radial-gradient(circle at 45% 40%, var(--mark-tint-front) 0%, rgba(11,100,120,0.08) 55%, rgba(11,100,120,0) 70%);
  }
  .wordmark {
    position: relative;
    font-weight: 300; letter-spacing: 0.06em; text-transform: uppercase; line-height: 1;
    white-space: nowrap;
  }
  .card--front .wordmark { color: var(--teal); font-size: 46px; margin-left: 60px; }
  .details { position: relative; }
  .divider {
    width: 34px; height: 4px; background: var(--teal); margin: 36px 0 16px;
  }
  .person__name { font-weight: 700; font-size: 19px; color: var(--teal); }
  .person__role { font-size: 15px; line-height: 1.35; color: var(--ink); }
  .contacts { list-style: none; margin-top: 18px; }
  .contacts li {
    display: flex; align-items: center; gap: 10px; font-size: 14.5px; line-height: 1.5; color: var(--ink);
  }
  .contacts svg { width: 14px; height: 14px; fill: var(--teal); flex: none; }
  /* Back */
  .card--back {
    background: linear-gradient(160deg, var(--teal-light) 0%, var(--teal) 45%, var(--teal-deep) 100%);
    padding: 150px 60px 0 0;
    display: flex; flex-direction: column; align-items: flex-end;
  }
  .card--back .brand-mark-area {
    left: -140px; top: -200px;
    background: radial-gradient(circle at 55% 55%, var(--mark-tint-back) 0%, rgba(255,255,255,0.06) 55%, rgba(255,255,255,0) 70%);
  }
  .card--back .wordmark { color: var(--white); font-size: 56px; }
  .card--back .website {
    position: relative; align-self: flex-start; margin: 44px 0 0 170px;
    color: var(--url-white); font-size: 15px; letter-spacing: 0.32em;
  }
</style>
</head>
<body>
<main class="canvas">
  <section class="card card--front" aria-label="Business card front">
    <div class="brand-mark-area" role="img" aria-label="Large brand symbol placement"></div>
    <h1 class="wordmark">Marlow Hire</h1>
    <div class="details">
      <div class="divider"></div>
      <p class="person__name">Clara Whitfield</p>
      <p class="person__role">Director<br>Senior Search Consultant</p>
      <ul class="contacts">
        <li>
          <svg viewBox="0 0 24 24" aria-hidden="true"><path d="M6.6 10.8a15.1 15.1 0 0 0 6.6 6.6l2.2-2.2a1 1 0 0 1 1-.25 11.4 11.4 0 0 0 3.6.57 1 1 0 0 1 1 1V20a1 1 0 0 1-1 1A17 17 0 0 1 3 4a1 1 0 0 1 1-1h3.5a1 1 0 0 1 1 1c0 1.250.2 2.45.57 3.57a1 1 0 0 1-.25 1z"/></svg>
          +64 21 555 0142
        </li>
        <li>
          <svg viewBox="0 0 24 24" aria-hidden="true"><path d="M2 5h20v14H2zm2 2v.5l8 5 8-5V7zm0 2.9V17h16V9.9l-8 5z"/></svg>
          clara@marlowhire.nz
        </li>
        <li>
          <svg viewBox="0 0 24 24" aria-hidden="true"><path d="M12 2a10 10 0 1 0 0 20 10 10 0 0 0 0-20zm0 2c.8 1.1 1.5 2.5 1.9 4h-3.8c.4-1.5 1.1-2.9 1.9-4zM4.3 14a8 8 0 0 1 0-4h3.4a16 16 0 0 0 0 4zm5.4 0a14 14 0 0 1 0-4h4.6a14 14 0 0 1 0 4zm6.6 0a16 16 0 0 0 0-4h3.4a8 8 0 0 1 0 4zM12 20c-.8-1.1-1.5-2.5-1.9-4h3.8c-.4 1.5-1.1 2.9-1.9 4z"/></svg>
          www.marlowhire.nz
        </li>
      </ul>
    </div>
  </section>

  <section class="card card--back" aria-label="Business card back">
    <div class="brand-mark-area" role="img" aria-label="Large brand symbol placement"></div>
    <h2 class="wordmark">Marlow Hire</h2>
    <p class="website">www.marlowhire.nz</p>
  </section>
</main>
</body>
</html>
```